Education portal needs a new Email Creative Design

We could not decide on the creative earlier as we were unable to picture how will it look. Hence, we have added content so that we can choose the best design of all. Below is the content to be used for the email creative:
____________________________________
Did you know that 25% of all Americans have experienced at least one divorce?*
41% of first marriages end in divorce!!*

Over 1 million children are affected by divorce each year*

Become a Marriage and Family therapist - Achieve inner-happiness by helping individuals, families and couples resolve their struggles and enhance their lives.
Family Therapists are trained in various modes of therapy in order to prepare them for work with individuals, families, couples, and groups.

With proper training, you will be able to treat:
• Depression and other Affective Disorders
• Childhood Behavioral and Emotional Disorders
• Marital and Relationship Problems
• Conduct Disorder and Delinquency
• Substance Abuse
• Alcoholism
• Domestic Violence
• Severe Mental Illness
• Physical Illness

You could also qualify for financial aid* from the government to pursue this career..

Secure your life by earning upto $78,580* and attain peace of mind while helping others..

__________________________

These are the links to images we liked, but if you have something better, we would love to see them:
http://www.pictovale.example/photo/seperated-50317294?st=7kq2m81
http://www.pictovale.example/photo/domestic-violence-68204937?st=b4n9x52

We are an education portal offering options of schools, colleges, universities and courses to students and working professionals.

We are looking for an email creative which has great call-to-action; be creative and research more if you wish.
Incorporate call-to-action tabs, make it colorful, include pictures and content.
Also attached are industry standard creatives for your reference, let me know if you have any questions.
Updates

Please see new files uploaded

I have uploaded a new creative made by our design team. Follow similar guidelines

For those who have not submitted their designs, please send us soon. Thanks

We thought a content brief will do more justice to this design contest hence we have updated our brief with new content to create a newer design Please submit your designs soon. Thanks

Target Market(s)

25 to 50 years working professionals

Industry/Entity Type

Government

Font styles to use
Serif
Sans Serif
Decorative
Script

Requirements
Must have
• Call-to-action

```html
<!DOCTYPE html>
<html lang="en">
<head>
<meta charset="utf-8">
<title>Marriage and Family Therapist Career Flyer</title>
<link href="https://fonts.googleapis.com/css2?family=Open+Sans:wght@400;600;700&display=swap" rel="stylesheet">
<style>
  :root{
    --page-bg:#ececec;
    --card-bg:#ffffff;
    --brand-red:#c8161d;
    --deep-red:#7a1a1c;
    --banner-red:#6b1f1d;
    --salmon:#e8836e;
    --body-grey:#555555;
    --logo-grey:#5a5a5a;
    --white:#ffffff;
  }
  *{margin:0;padding:0;box-sizing:border-box}
  html,body{width:857px;height:1200px;overflow:hidden;background:var(--page-bg)}
  body{position:relative;font-family:"Open Sans",Arial,sans-serif;color:var(--body-grey)}
  .flyer-shapes{position:absolute;left:0;top:0;width:857px;height:1200px}
  .abs{position:absolute;white-space:nowrap}
  .headline{left:50px;color:var(--white);font-weight:600;letter-spacing:.2px}
  .headline--one{top:296px;font-size:24px}
  .headline--two{top:334px;font-size:35px;font-weight:700;color:var(--brand-red)}
  .headline--three{top:378px;font-size:30px}
  .cta-title{left:440px;width:392px;text-align:center;top:512px;font-size:45px;color:var(--white);font-weight:400}
  .cta-phone{left:440px;width:392px;text-align:center;top:566px;font-size:38px;color:var(--white);font-weight:400}
  .fact{left:48px;font-size:13.5px;font-weight:600;color:var(--brand-red);line-height:18px}
  .intro{left:48px;top:682px;width:470px;font-size:13px;line-height:21.2px;white-space:normal}
  .banner-text{left:48px;top:783px;font-size:13px;font-weight:700;color:var(--white)}
  .treat-list{left:48px;top:816px;list-style:none;font-size:13px;line-height:21.2px}
  .treat-list li::before{content:"• "}
  .earnings{left:48px;top:1007px;font-size:14px;font-weight:700;color:var(--brand-red)}
  .brand-name{left:60px;top:1040px;font-size:46px;font-weight:400;color:var(--logo-grey)}
  .contact{font-size:13px;color:var(--body-grey)}
</style>
</head>
<body>
<svg class="flyer-shapes" viewBox="0 0 857 1200" aria-hidden="false">
  <defs>
    <linearGradient id="heroTone" x1="0" y1="0" x2="1" y2="1">
      <stop offset="0" stop-color="#3a2622"/>
      <stop offset="0.45" stop-color="#8a6a5c"/>
      <stop offset="1" stop-color="#2a1c1a"/>
    </linearGradient>
    <linearGradient id="insetTone" x1="0" y1="0" x2="1" y2="1">
      <stop offset="0" stop-color="#2c4a56"/>
      <stop offset="0.5" stop-color="#6f8c8e"/>
      <stop offset="1" stop-color="#1d3038"/>
    </linearGradient>
  </defs>
  <rect x="25" y="78" width="807" height="1044" fill="var(--card-bg)"/>

  <rect x="25" y="78" width="807" height="558" fill="url(#heroTone)" role="img" aria-label="Photograph of a frightened young girl held by an adult's hands"/>

  <path d="M60 95 H180 Q200 95 214 110 L440 345 Q455 362 440 378 L210 595 Q195 610 175 610 H60 Q35 610 35 585 V120 Q35 95 60 95 Z" fill="#8c2a22" opacity="0.55"/>
  <path d="M25 200 L240 200 L545 345 L300 600 L25 600 Z" fill="#a5392f" opacity="0.25"/>
  <path d="M505 492 H832 V636 H440 L490 510 Q497 492 505 492 Z" fill="#c26a5e" opacity="0.82"/>

  <path d="M590 676 H660 L508 830 L655 985 H590 L440 830 Z" fill="var(--deep-red)"/>
  <path d="M610 660 H832 V998 H640 L508 830 Z" fill="url(#insetTone)" role="img" aria-label="Photograph of a distressed woman hiding her face with her arm"/>

  <path d="M25 778 H343 L360 792 L343 806 H25 Z" fill="var(--banner-red)"/>
  <path d="M348 778 L365 792 L348 806" fill="none" stroke="var(--salmon)" stroke-width="3"/>

  <path d="M522 1053 H530 L535 1059 L530 1065 H522 Z" fill="var(--brand-red)"/>
  <path d="M660 1053 H668 L673 1059 L668 1065 H660 Z" fill="var(--brand-red)"/>
  <path d="M522 1075 H530 L535 1081 L530 1087 H522 Z" fill="var(--brand-red)"/>
</svg>

<div class="abs headline headline--one">OVER 1 MILLION CHILDREN</div>
<div class="abs headline headline--two">ARE AFFECTED BY</div>
<div class="abs headline headline--three">DIVORCE EACH YEAR</div>

<div class="abs cta-title">Call Now</div>
<div class="abs cta-phone">1800 - 000 - 0000</div>

<p class="abs fact" style="top:645px">Did you know that 25% of all Americans have experienced at least one divorce?</p>
<p class="abs fact" style="top:663px">41% of first marriages end in divorce!!</p>
<p class="abs intro">Become a Marriage and Family therapist - Achieve inner-happiness by helping individuals, families and couples resolve their struggles and enhance their lives. Family Therapists are trained in various modes of therapy in order to prepare them for work with individuals, families, couples, and groups.</p>

<div class="abs banner-text">With proper training, you will be able to treat:</div>
<ul class="abs treat-list">
  <li>Depression and other Affective Disorders</li>
  <li>Childhood Behavioral and Emotional Disorders</li>
  <li>Marital and Relationship Problems</li>
  <li>Conduct Disorder and Delinquency</li>
  <li>Substance Abuse</li>
  <li>Alcoholism</li>
  <li>Domestic Violence</li>
  <li>Severe Mental Illness</li>
  <li>Physical Illness</li>
</ul>

<p class="abs earnings">Secure your life by earning upto $78,580* and attain peace of mind while helping others..</p>

<div class="abs brand-name">YOUR LOGO</div>
<div class="abs contact" style="left:545px;top:1050px">(201) 000 - 0000</div>
<div class="abs contact" style="left:684px;top:1050px">www.yourweb.com</div>
<div class="abs contact" style="left:545px;top:1072px">100, Linden Grove Drive, Fairhaven, NY 10012</div>
</body>
</html>
```